Laundry pickup and delivery flyer "Fold Harbor laundry"

I need a flyer "8.5"x11" that tells customers about our pickup and delivery laundry service. our website address is: www.foldharborlaundry.example The flyer should be front and back.

Font styles to use
Sans Serif

Colors
0094D4
00A9DD
6FCCEA
C7EBF8
E9F6FB

```html
<!DOCTYPE html>
<html lang="en">
<head>
<meta charset="utf-8">
<title>Fold Harbor laundry – Pickup &amp; Delivery Flyer</title>
<link href="https://fonts.googleapis.com/css2?family=Fira+Sans:wght@400;500;600;700;800&display=swap" rel="stylesheet">
<style>
  :root{
    --navy:#0b2aa6;
    --ink:#1b3c9e;
    --blue:#0094d4;
    --sky:#00a9dd;
    --cyan:#1fc3ea;
    --aqua:#6fccea;
    --ice:#c7ebf8;
    --mist:#e9f6fb;
    --mint:#45efdc;
    --panel:#9ef6fb;
    --white:#ffffff;
  }
  *{box-sizing:border-box;margin:0;padding:0}
  html,body{width:1200px;height:760px;overflow:hidden;background:#fff}
  body{position:relative;font-family:"Fira Sans",Arial,sans-serif;color:var(--ink)}
  .side-label{position:absolute;top:-4px;font:400 22px Arial,sans-serif;color:#111;width:200px;text-align:center}
  .side-label.front{left:185px}
  .side-label.back{left:815px}

  .page{position:absolute;top:24px;width:570px;height:736px;overflow:hidden;background:#fff;border:1px solid #bbb}
  .page.front{left:0}
  .page.back{left:630px}

  /* front */
  .beach-scene{position:absolute;left:0;top:0;width:570px;height:396px;
    background:radial-gradient(ellipse at 45% 62%,#8af3ef 0%,#2ed6f0 35%,#1a8cf0 100%)}
  .laundry-basket{position:absolute;left:24px;top:258px;width:222px;height:184px;border-radius:60px 60px 24px 24px;
    background:linear-gradient(180deg,#7fa6d8 0%,#9fb7e0 38%,#e6edf4 58%,#f5f7fa 100%)}
  .tagline{position:absolute;left:28px;top:176px;color:#fff;font-weight:600;font-size:33px;line-height:43px;letter-spacing:1px;
    text-shadow:1px 2px 3px rgba(0,0,0,.55)}
  .brand-mark{position:absolute;left:0;top:478px;width:570px;display:flex;justify-content:center;align-items:center;gap:10px}
  .brand-mark .dot{width:22px;height:22px;border-radius:50%;background:var(--sky)}
  .brand-mark .name{font-weight:700;font-size:34px;color:var(--blue)}
  .van-photo{position:absolute;left:2px;top:594px;width:296px;height:130px;border-radius:24px 50px 18px 18px;
    background:linear-gradient(90deg,#2a6fe0 0%,#4aa6f0 35%,#f4f7fb 58%,#e9edf2 100%)}
  .offer{position:absolute;left:300px;top:548px;width:260px;text-align:center;color:var(--ink);font-weight:600}
  .offer .free{font-size:31px;line-height:30px}
  .offer .service{font-size:31px;line-height:30px;white-space:nowrap}
  .front-call{position:absolute;right:16px;top:699px;font-weight:600;font-size:19px;color:var(--ink)}
  .wave{position:absolute;left:0;bottom:0}

  /* back */
  .top-wave{position:absolute;left:0;top:0}
  .headline{position:absolute;left:0;width:570px;text-align:center}
  .brand-title{top:80px;font-size:56px;font-weight:700;color:var(--navy);letter-spacing:1px;line-height:60px}
  .brand-sub{top:140px;font-size:29px;font-weight:600;color:var(--navy)}
  .brand-claim{top:190px;font-size:19px;font-weight:500;color:var(--cyan)}
  .brand-claim.second{top:221px}
  .service-band{position:absolute;left:0;top:249px;width:570px;height:31px;
    background:linear-gradient(90deg,var(--navy) 0%,#1b46c8 45%,var(--mint) 100%);
    color:#fff;font-size:25px;font-weight:500;text-align:center;line-height:31px}
  .laundromat-scene{position:absolute;left:0;top:296px;width:570px;height:190px;
    background:linear-gradient(90deg,#ffffff 0%,#c9ccd3 25%,#bfc3cb 35%,#ffffff 48%,#e7eaef 65%,#c3c7cf 85%,#ffffff 100%)}
  .floor-line{position:absolute;left:0;top:486px;width:570px;height:3px;background:var(--navy)}
  .steps{position:absolute;left:22px;top:506px;width:527px;display:grid;grid-template-columns:258px 258px;column-gap:10px;row-gap:19px}
  .step{height:58px;background:var(--panel);display:flex;align-items:center;border-radius:29px 0 0 29px}
  .step .icon{flex:none;width:58px;height:58px;border-radius:50%;background:#fff;border:4px solid #c5fbfd;display:flex;align-items:center;justify-content:center}
  .step p{font-size:11.4px;line-height:14px;color:#111;padding-left:4px;padding-right:2px;letter-spacing:-.1px}
  .back-footer{position:absolute;left:0;top:650px;width:570px;height:86px;
    background:linear-gradient(180deg,rgba(233,246,251,0) 0%,var(--aqua) 55%,var(--sky) 100%)}
  .call-line{position:absolute;left:0;top:668px;width:570px;text-align:center;font-size:32px;font-weight:700;color:var(--ink)}
  .web-line{position:absolute;left:0;top:714px;width:570px;text-align:center;font-size:15px;color:#fff;letter-spacing:3px}
</style>
</head>
<body>
  <div class="side-label front">FRONT</div>
  <div class="side-label back">BACK</div>

  <section class="page front">
    <div class="beach-scene" role="img" aria-label="Beach holiday illustration: 'Happy Holidaying' script lettering, striped umbrella, deck chair, life ring, beach ball, sandals and palm leaves on a bright blue background"></div>
    <div class="laundry-basket" role="img" aria-label="Photo of a white laundry basket piled with colourful clothes"></div>
    <div class="tagline">YOU LEAVE IT<br>WE CLEAN IT</div>

    <div class="brand-mark">
      <span class="dot"></span>
      <span class="name">Fold Harbor laundry</span>
    </div>

    <svg class="wave" width="570" height="100" viewBox="0 0 570 100" aria-hidden="true">
      <defs>
        <linearGradient id="frontWave" x1="0" y1="0" x2="1" y2="0">
          <stop offset="0" stop-color="#c7fbfd"/>
          <stop offset="1" stop-color="#45efdc"/>
        </linearGradient>
      </defs>
      <path d="M300 100 C360 80 400 20 470 12 C510 8 545 14 570 20 L570 100 Z" fill="url(#frontWave)"/>
      <path d="M0 100 C60 80 120 84 170 100 Z" fill="#c7fbfd"/>
    </svg>

    <div class="van-photo" role="img" aria-label="Photo of the branded blue and white pickup and delivery van"></div>

    <div class="offer">
      <div class="free">FREE</div>
      <div class="service">Pickup &amp; Delivery</div>
    </div>

    <div class="front-call">call us at 555-014-0199</div>
  </section>

  <section class="page back">
    <svg class="top-wave" width="570" height="120" viewBox="0 0 570 120" aria-hidden="true">
      <path d="M0 0 L570 0 C540 20 500 20 470 18 C420 14 330 -10 230 24 C170 44 150 72 100 84 C60 94 20 92 0 90 Z" fill="#c2fbf5"/>
      <path d="M0 0 L140 0 C110 30 80 60 40 80 C20 88 8 90 0 90 Z" fill="#45efdc"/>
    </svg>

    <div class="headline brand-title">FOLD HARBOR</div>
    <div class="headline brand-sub">Jackson’s Premier Laundry Service</div>
    <div class="headline brand-claim">Mississippi’s most Advanced &amp; Professional Laundry Service</div>
    <div class="headline brand-claim second">Instant Pickup &amp; Delivery System</div>

    <div class="service-band">Residential &amp; Commercial Services</div>

    <div class="laundromat-scene" role="img" aria-label="Illustration of two washing machines with laundry baskets and detergent, and a customer reading on a bench while she waits"></div>
    <div class="floor-line"></div>

    <div class="steps">
      <div class="step">
        <div class="icon">
          <svg width="38" height="38" viewBox="0 0 38 38" aria-hidden="true"><circle cx="19" cy="19" r="16" fill="none" stroke="#0b2aa6" stroke-width="3"/><path d="M19 9 V19 L26 23" fill="none" stroke="#0b2aa6" stroke-width="2.5" stroke-linecap="round"/></svg>
        </div>
        <p>Schedule a pickup - feel free to leave your bag where our driver can get to it.</p>
      </div>
      <div class="step">
        <div class="icon">
          <svg width="40" height="30" viewBox="0 0 40 30" aria-hidden="true"><path d="M3 6 H24 L32 13 L37 15 V23 H3 Z" fill="none" stroke="#0b2aa6" stroke-width="2.2" stroke-linejoin="round"/><circle cx="11" cy="24" r="3.5" fill="#fff" stroke="#0b2aa6" stroke-width="2"/><circle cx="30" cy="24" r="3.5" fill="#fff" stroke="#0b2aa6" stroke-width="2"/></svg>
        </div>
        <p>Our driver will pickup your clothes at the scheduled time.</p>
      </div>
      <div class="step">
        <div class="icon">
          <svg width="30" height="36" viewBox="0 0 30 36" aria-hidden="true"><rect x="2" y="2" width="26" height="32" rx="3" fill="none" stroke="#0b2aa6" stroke-width="2"/><line x1="2" y1="9" x2="28" y2="9" stroke="#0b2aa6" stroke-width="2"/><circle cx="15" cy="21" r="8" fill="none" stroke="#0b2aa6" stroke-width="2"/><path d="M9 22 Q15 18 21 22 A6 6 0 0 1 9 22Z" fill="#0b2aa6"/></svg>
        </div>
        <p>Your clothes are expertly cleaned by our team of laundry professionals.</p>
      </div>
      <div class="step">
        <div class="icon">
          <svg width="40" height="34" viewBox="0 0 40 34" aria-hidden="true"><path d="M16 6 A4 4 0 1 1 20 11 V14 L37 24 H3 L20 14" fill="none" stroke="#0b2aa6" stroke-width="2.2" stroke-linejoin="round"/><rect x="9" y="24" width="22" height="8" fill="none" stroke="#0b2aa6" stroke-width="2"/></svg>
        </div>
        <p>We delivery your clean clothes back to you at your convenience!</p>
      </div>
    </div>

    <div class="back-footer"></div>
    <div class="call-line">CALL US AT : 555-014-0199</div>
    <div class="web-line">www.foldharborlaundry.example</div>
  </section>
</body>
</html>
```